Travel Blogger Business Card for roamquill.net

I need a two-sided business card for a travel blogging website. The card should be both professional and fun at the same time. This is for the website www.roamquill.net

I don't necessarily think that the current logo on the website needs to be used on the business card but it can be. I am very flexible with ideas

Target Market(s)

Travel agencies that will be met at a conference.

Industry/Entity Type

Travel

Contact Information for Business Card

Company Name: Roam Quill.net
Name: Bertrand Olesky
Voice: +1-(345)-402-7731
Address: Coral Reach Shore, Grand Cayman, Cayman Islands
Email: ceo@roamquill.net

Colors
0592cd
0355a3
3176b5
33a6d7
85cae6
85acd3

Requirements
Must have
• Website address and name should be bigger than address, phone number, and email.

```html
<!DOCTYPE html>
<html lang="en">
<head>
<meta charset="utf-8">
<title>Roam Quill.net – Business Card</title>
<link href="https://fonts.googleapis.com/css2?family=Roboto+Condensed:wght@300;400;700&family=Roboto:wght@300;400&display=swap" rel="stylesheet">
<style>
  :root {
    --stage: #2a2a2c;
    --card-light: #ffffff;
    --card-dark: #1c1c1e;
    --brand-blue: #33a6d7;
    --text-grey: #5a5a5c;
    --rule-grey: #9a9a9c;
    --mark-grey: #4a4a4c;
    --web-light: #d8d8d8;
  }
  * { box-sizing: border-box; margin: 0; padding: 0; }
  html, body { width: 1200px; height: 950px; overflow: hidden; }
  body {
    background: var(--stage);
    display: flex;
    flex-direction: column;
    align-items: center;
    justify-content: center;
    gap: 64px;
    font-family: "Roboto", Arial, sans-serif;
  }
  .card {
    width: 600px;
    height: 343px;
    position: relative;
    box-shadow: 0 10px 30px rgba(0,0,0,.45);
  }
  .card--front { background: var(--card-light); }
  .card--back { background: var(--card-dark); }

  .brand {
    display: flex;
    align-items: center;
    gap: 10px;
    font-family: "Roboto Condensed", "Arial Narrow", sans-serif;
    font-weight: 700;
    color: var(--brand-blue);
    text-transform: uppercase;
    letter-spacing: .5px;
    line-height: 1;
  }
  .brand__dot { border-radius: 50%; background: var(--mark-grey); flex: none; }

  .card--front .brand { position: absolute; left: 70px; top: 78px; font-size: 46px; }
  .card--front .brand__dot { width: 34px; height: 34px; }

  .name-rule {
    position: absolute; left: 40px; right: 40px; top: 176px;
    display: flex; align-items: center; gap: 16px;
  }
  .name-rule::before, .name-rule::after {
    content: ""; flex: 1; height: 1px; background: var(--rule-grey);
  }
  .name-rule__name {
    font-family: "Roboto Condensed", "Arial Narrow", sans-serif;
    font-weight: 400; font-size: 21px; letter-spacing: .5px;
    color: var(--brand-blue); text-transform: uppercase;
  }

  .contact {
    position: absolute; left: 40px; bottom: 36px;
    list-style: none; font-weight: 300; font-size: 15px; color: var(--text-grey);
    display: flex; flex-direction: column; gap: 6px;
  }
  .contact li { display: flex; align-items: center; gap: 10px; }
  .contact svg { width: 13px; height: 13px; fill: var(--brand-blue); flex: none; }

  .address {
    position: absolute; right: 40px; bottom: 36px;
    font-style: normal; font-weight: 300; font-size: 15px; line-height: 1.45;
    color: var(--text-grey); text-align: right;
  }

  .card--back .brand {
    position: absolute; left: 50%; top: 120px; transform: translateX(-50%);
    font-size: 56px; white-space: nowrap;
  }
  .card--back .brand__dot { width: 40px; height: 40px; background: #ffffff; }
  .card--back .website {
    position: absolute; left: 0; right: 0; top: 220px; text-align: center;
    font-weight: 300; font-size: 14px; letter-spacing: 5px; color: var(--web-light);
  }
</style>
</head>
<body>

  <section class="card card--front" aria-label="Business card front">
    <div class="brand"><span class="brand__dot"></span><span class="brand__name">Roam Quill</span></div>

    <div class="name-rule"><span class="name-rule__name">Bertrand Olesky</span></div>

    <ul class="contact">
      <li>
        <svg viewBox="0 0 16 16" aria-hidden="true"><path d="M3.6 1.2l2.3 2.3-1.4 2a9 9 0 0 0 6 6l2-1.4 2.3 2.3-1.6 2.4C7.6 14.6 1.4 8.4 1.2 2.8z"/></svg>
        +1-(345)-402-7731
      </li>
      <li>
        <svg viewBox="0 0 16 16" aria-hidden="true"><path d="M1 3h14v10H1zM2 4v.6l6 4 6-4V4z" fill-rule="evenodd"/></svg>
        ceo@roamquill.net
      </li>
      <li>
        <svg viewBox="0 0 16 16" aria-hidden="true"><circle cx="8" cy="8" r="7"/></svg>
        www.roamquill.net
      </li>
    </ul>

    <address class="address">Coral Reach Shore<br>Grand Cayman<br>Cayman Islands</address>
  </section>

  <section class="card card--back" aria-label="Business card back">
    <div class="brand"><span class="brand__dot"></span><span class="brand__name">Roam Quill</span></div>
    <p class="website">www.roamquill.net</p>
  </section>

</body>
</html>
```